program promotional Information booklets used for marketing and information

We need someone to take our two word documents and work some graphic design magic to make it look more professional and inviting. These documents are used for potential new customers. Our target audience is youth and young adults with disabilities and their families. Our website will help to provide our current style www.brightharbourway.com.au and our logo will set the colour palette. We want the booklets to convey a culture of fun, innovation, energy & creativity. We do not want to look like a corporate or formal organisation. We want to look more organic and grassroots. The booklets will be distributed as electronic documents and printed in-house. Ideally we would like to still be able to edit the final document in case our prices or services change in the future.

Target Market(s)

Youth and Young adults with special needs

Industry/Entity Type

Community Service

Font styles to use
Sans Serif

Requirements
Must have
• The photos provided relate to the Waterfall booklet. This program is for those with more profound disabilities. The Pebble program is for those with less support needs, generally not in wheelchairs, but who may have some mobility challenges and mild intellectual disabilities. As you will see our business name is Bright Harbour and this is what we attempt to do for all the young people we work with. We do not focus on their disability but rather on their unique abilities and what they can achieve. In both programs we look to achieve social inclusion in the general community as much as possible.
Nice to have
• Wants to feel high energy, fun, innovative and creative. Could use some stock images in the Pebble booklet if you wanted to. Some of the activities this program will do include: organic gardening, cooking, music, dance and drama, art, life skills, mastering public transport, exercise, etc.
Should not have
• should not focus on disability stereotypes. Should not be too childish.

```html
<!DOCTYPE html>
<html lang="en">
<head>
<meta charset="utf-8">
<title>Bright Harbour – Information Booklet Page</title>
<link rel="stylesheet" href="https://fonts.googleapis.com/css2?family=Carlito:wght@400;700&display=swap">
<style>
  :root {
    --teal: #4bafb1;
    --green: #8cc63f;
    --red: #c1272d;
    --yellow: #fff200;
    --ink: #1a1a1a;
    --page: #ffffff;
  }
  * { box-sizing: border-box; margin: 0; padding: 0; }
  html, body { width: 848px; height: 1200px; overflow: hidden; background: var(--page); }
  .page {
    position: relative;
    width: 848px;
    height: 1200px;
    overflow: hidden;
    font-family: "Carlito", "Calibri", sans-serif;
    color: var(--ink);
    font-size: 15.7px;
    line-height: 22.8px;
  }
  .edge-band { position: absolute; }
  .edge-band--left {
    left: 0; top: 0; width: 44px; height: 490px;
    background: linear-gradient(to bottom,
      var(--teal) 0%, var(--green) 22%, var(--red) 42%,
      var(--teal) 58%, var(--yellow) 72%, var(--teal) 88%);
  }
  .edge-band--right {
    right: 0; top: 727px; width: 44px; height: 473px;
    background: linear-gradient(to bottom,
      var(--teal) 0%, var(--yellow) 18%, var(--teal) 38%,
      var(--red) 55%, var(--green) 75%, var(--teal) 95%);
  }
  .content {
    position: absolute;
    left: 60px;
    top: 139px;
    width: 733px;
  }
  .service-list { list-style: none; margin-bottom: 36px; }
  .service-list li { position: relative; padding-left: 88px; }
  .service-list li::before {
    content: ""; position: absolute; left: 71px; top: 9px;
    width: 6px; height: 6px; border-radius: 50%; background: var(--ink);
  }
  p { margin-bottom: 13px; }
  .section-title { font-size: 15.7px; line-height: 22.8px; font-weight: 700; }
  .intro-text { margin-bottom: 13px; }
  .commitments { list-style: none; margin: 0 0 14px 0; }
  .commitments li { position: relative; padding-left: 88px; margin-bottom: 18px; }
  .commitments li:last-child { margin-bottom: 0; }
  .commitments li::before {
    content: ""; position: absolute; left: 69px; top: 8px;
    width: 7px; height: 7px; border-radius: 50%; border: 1px solid var(--ink);
  }
  .values p { margin-bottom: 18px; }
  .value-name { font-weight: 700; }
</style>
</head>
<body>
<div class="page">
  <div class="edge-band edge-band--left" role="img" aria-label="Cluster of overlapping teal, green, red and yellow pentagon shapes along the left edge"></div>
  <div class="edge-band edge-band--right" role="img" aria-label="Cluster of overlapping teal, yellow, red and green pentagon shapes along the right edge"></div>

  <main class="content">
    <ul class="service-list">
      <li>In-home support either one-on-one or for a small group of people based on existing friendships or support clusters</li>
      <li>Centre based activities at our hubs, ranging from one-on-one support through to our Pebble small group program</li>
      <li>A combination of all of the above</li>
    </ul>

    <p>We do not offer a one size fits all model because it doesn’t work! Instead we work with each individual to develop a unique plan which is based around their goals and passions.</p>

    <h2 class="section-title">Eligibility</h2>
    <p>Bright Harbour works with all people with a disability aged 0-65 years and their families and carers. That said, we have specialist skills in working with young people who are aged 0-35 years.</p>

    <h2 class="section-title">Why we exist</h2>
    <p class="intro-text">It is our passion to bring about transformation to the way disability services are currently delivered. For over twenty years we have observed and experienced the commercialisation and commodification of disability care. We have felt first-hand the frustration of service limitations and provider’s supports driven solely by funding.</p>

    <ul class="commitments">
      <li>We believe that there must be a better way and are committed to exploring it</li>
      <li>We are committed to travelling with families to find creative solutions to everyday challenges</li>
      <li>We are committed to empowering families to triumph over the ‘disability system’ which rather than provide the necessary supports more often appears to be a blockage or source of frustration</li>
    </ul>

    <section class="values">
      <h2 class="section-title">Our Core Values</h2>
      <p><span class="value-name">ENABLE</span> – We exist to enable and facilitate young people and their families to receive high quality services. We can act as the conduit which can connect you to the right person at the right time so that small challenges don’t become big barriers. If we can’t provide the service we’re not afraid to link you with someone else who knows more about your area of need then we do.</p>

      <p><span class="value-name">EMPOWER</span> – We seek to empower young people and their families to have maximum control and optimal choice about the future. We want the best for your future and will plan and work with you to achieve it.</p>

      <p><span class="value-name">INNOVATE</span> – We want to excel at finding new and different ways to approach problems and help you achieve your goals. We won’t settle for simply doing things the conventional way but will look for better and more effective solutions and approaches to the challenges you face.</p>
    </section>
  </main>
</div>
</body>
</html>
```